High quality health product needs a label

If you are a top professional designer for exclusive product labels, please read on.

High quality health products are being filled into so called Quorel glass bottles (see attachment) and I want to create labels for a range of different herbs (i.e. teasel, artemesia annua) in various dosage forms (i.e. liquid, capsules and tea). The brand of these products is called velmondra.

The label for each type of herb shall have a small variance in color, i.e. teasel can have some violet and artemesia annua a green theme. The variance in color should be unique (not just 2 circles and a triangle) and abstract (i.e. no leafs). Please have a look at 2 of our labels we have created for other products.

The logo I feel comfortable with is attached in the file plindaloft. I only want to take the leaf as logo, nothing else. The color of the logo should be adapted to our needs, but a green leaf makes sense to me. The color of the logo does not change for the variations of the label.

What do I expect in terms of design:

- minimalistic
- exclusive
- luxury
- classy
- abstract
- playful
- uniqueness

The front of the label should show:
- logo
- name of the herb, i.e. teasel
- dosage form, i.e. extract
- content, i.e. 250 ml
- the 2 logos to indicate that the product is certified organic

The back will contain some basic information that I will provide once I selected your design.

The final deliverables are 4 illustrator (compatible with version 16) ai vector files for 4 different types of herbs. Once the initial design is set, we need to create 3 color variations.

Please use a 100 mm x 210 mm layout for the 500 ml syrup bottle.

Target Market(s)

people with an interest in their health

Industry/Entity Type

health

Font styles to use
Sans Serif

Requirements
Must have
• abstract, unique, luxury, high class, minimalistic
Should not have
• overloaded, too many colors,

```html
<!DOCTYPE html>
<html lang="en">
<head>
<meta charset="utf-8">
<title>Teasel Extract – velmondra label</title>
<link rel="stylesheet" href="https://fonts.googleapis.com/css2?family=Playfair+Display:wght@500;600&family=Montserrat:wght@300;500&display=swap">
<style>
  :root {
    --page-bg: #eeeef2;
    --label-bg: #ffffff;
    --label-edge: #2a2a2a;
    --brand-green: #1f6a2c;
    --herb-violet: #8458ee;
    --herb-violet-deep: #6a3de0;
    --wash-light: #c7b2fa;
    --wash-mid: #9a70f2;
    --wash-deep: #8a5cf0;
    --ink: #1b1b1b;
    --badge-white: #ffffff;
    --badge-green: #8cc63e;
    --badge-red: #c8323a;
  }
  * { margin: 0; padding: 0; box-sizing: border-box; }
  html, body {
    width: 1200px;
    height: 1200px;
    overflow: hidden;
    background: var(--page-bg);
  }
  .label {
    position: absolute;
    left: 50px;
    top: 338px;
    width: 1100px;
    height: 523px;
    background: var(--label-bg);
    border: 1px solid var(--label-edge);
    overflow: hidden;
  }
  .brand {
    position: absolute;
    top: 30px;
    left: 0;
    width: 100%;
    display: flex;
    justify-content: center;
    align-items: center;
    gap: 10px;
    font-family: "Montserrat", sans-serif;
    font-weight: 500;
    font-size: 26px;
    letter-spacing: 1px;
    color: var(--brand-green);
  }
  .brand-dot {
    width: 14px;
    height: 14px;
    border-radius: 50%;
    background: var(--brand-green);
  }
  .herb-name {
    position: absolute;
    top: 200px;
    left: 0;
    width: 100%;
    text-align: center;
    font-family: "Playfair Display", serif;
    font-weight: 600;
    font-size: 84px;
    line-height: 1;
    letter-spacing: -2px;
    color: var(--herb-violet);
  }
  .dosage-form {
    position: absolute;
    top: 270px;
    left: 0;
    width: 100%;
    text-align: center;
    font-family: "Playfair Display", serif;
    font-weight: 500;
    font-size: 42px;
    line-height: 1;
    letter-spacing: -1px;
    color: var(--ink);
  }
  .color-wash {
    position: absolute;
    left: 352px;
    top: 343px;
    width: 399px;
    height: 180px;
    background:
      radial-gradient(ellipse 60% 40% at 55% 30%, var(--wash-deep), transparent 80%),
      linear-gradient(to bottom, rgba(255,255,255,0) 0%, var(--wash-light) 12%, var(--wash-mid) 45%, var(--wash-deep) 100%);
    border-radius: 40% 45% 0 0 / 18% 22% 0 0;
  }
  .volume {
    position: absolute;
    left: 363px;
    top: 484px;
    font-family: "Montserrat", sans-serif;
    font-weight: 300;
    font-size: 22px;
    letter-spacing: 1px;
    color: var(--badge-white);
  }
  .organic-badges {
    position: absolute;
    left: 640px;
    top: 478px;
    display: flex;
    align-items: center;
    gap: 14px;
  }
  .badge-round {
    width: 32px;
    height: 32px;
    border-radius: 50%;
    background: var(--badge-white);
    border: 2px solid var(--badge-red);
  }
  .badge-leafbox {
    width: 42px;
    height: 28px;
    background: var(--badge-green);
  }
</style>
</head>
<body>
  <main class="label">
    <div class="brand"><span class="brand-dot"></span>velmondra</div>
    <h1 class="herb-name">Teasel</h1>
    <p class="dosage-form">Extract</p>
    <div class="color-wash" role="img" aria-label="Abstract violet watercolour wash"></div>
    <p class="volume">250 ml</p>
    <div class="organic-badges">
      <span class="badge-round" aria-label="Organic certification badge"></span>
      <span class="badge-leafbox" aria-label="Organic certification badge"></span>
    </div>
  </main>
</body>
</html>
```